Church Grand Opening Bill Board design

I would like to create a bill board design for our church's grand opening. I would like to incorporate pictures of two separate preachers with a creative way of blending them both together so it won't take up too much space. I have included pictures and logo.

I am open for color coordination and I have included a couple of past designs to use as a reference

The information I would want on the Build Board is the following (1) Grand Opening (2) 4218 E. Marlowe Avenue (3) 10:30am (4) Multi-Ethnic Church Planting Church (5) Sept. 26, 2021

Target Market(s)

Church shoppers and those who have never been connected to a church

Font styles to use
Serif

Requirements
Must have
• Our Logo
Nice to have
• i do not want any crosses or religious symbols

```html
<!DOCTYPE html>
<html lang="en">
<head>
<meta charset="UTF-8">
<title>Thrive Church Grand Opening Billboard</title>
<link href="https://fonts.googleapis.com/css2?family=Roboto+Slab:wght@400;500;700&display=swap" rel="stylesheet">
<style>
  :root {
    --page-bg: #ffffff;
    --board-dark: #1e1c1a;
    --board-brown: #3e2611;
    --brand-orange: #cf6a06;
    --ring-white: #ffffff;
    --ink-dark: #1e1c1a;
    --figure-light: #5a4030;
    --figure-dark: #1c1816;
  }
  html, body {
    margin: 0;
    padding: 0;
    width: 947px;
    height: 1200px;
    overflow: hidden;
    background: var(--page-bg);
  }
  .canvas {
    position: relative;
    width: 947px;
    height: 1200px;
    display: flex;
    align-items: center;
    justify-content: center;
  }
  .billboard {
    width: 900px;
    height: 417px;
    display: block;
    filter: drop-shadow(6px 10px 8px rgba(0, 0, 0, 0.45));
  }
  .billboard text {
    font-family: "Roboto Slab", Georgia, serif;
    text-anchor: middle;
  }
  .church-name { font-size: 46px; font-weight: 400; fill: var(--ink-dark); }
  .headline { font-size: 58px; font-weight: 700; fill: var(--ring-white); }
  .event-time { font-size: 36px; font-weight: 400; fill: var(--ink-dark); }
  .event-address { font-size: 27px; font-weight: 500; fill: var(--ring-white); }
  .tagline { font-size: 27px; font-weight: 400; fill: var(--ring-white); }
</style>
</head>
<body>
<main class="canvas">
  <svg class="billboard" viewBox="0 0 1044 484" xmlns="http://www.w3.org/2000/svg" aria-label="Thrive Church grand opening billboard">
    <defs>
      <linearGradient id="board-gradient" x1="0" y1="0" x2="1" y2="0">
        <stop offset="0" stop-color="var(--board-dark)"/>
        <stop offset="0.55" stop-color="#2a2017"/>
        <stop offset="1" stop-color="var(--board-brown)"/>
      </linearGradient>
      <linearGradient id="figure-gradient" x1="0" y1="0" x2="0" y2="1">
        <stop offset="0" stop-color="var(--figure-light)"/>
        <stop offset="1" stop-color="var(--figure-dark)"/>
      </linearGradient>
      <clipPath id="board-clip"><rect x="0" y="0" width="1044" height="484"/></clipPath>
      <clipPath id="badge-clip"><circle cx="314" cy="250" r="258"/></clipPath>
    </defs>

    <g class="board" clip-path="url(#board-clip)">
      <rect class="board-background" x="0" y="0" width="1044" height="484" fill="url(#board-gradient)"/>

      <g class="preachers-photo" role="img" aria-label="Photo of the two preachers standing side by side, one speaking with a headset and one smiling">
        <path d="M595 484 V160 Q595 120 640 110 L680 100 V40 Q680 0 730 0 Q780 0 780 40 V100 L830 115 Q850 122 850 160 V484 Z" fill="url(#figure-gradient)"/>
        <path d="M770 484 V170 Q770 130 820 118 L860 108 V55 Q860 15 910 15 Q960 15 960 55 V108 L1010 120 Q1044 130 1044 170 V484 Z" fill="url(#figure-gradient)"/>
      </g>

      <g class="orbit-lines" fill="none" stroke="var(--brand-orange)" stroke-width="3">
        <path d="M77 48 A305 305 0 0 0 140 484"/>
        <path d="M552 56 A305 305 0 0 1 583 365"/>
      </g>
      <g class="orbit-dots" fill="var(--ring-white)">
        <circle cx="77" cy="48" r="9"/>
        <circle cx="552" cy="56" r="9"/>
        <circle cx="583" cy="365" r="9"/>
      </g>

      <circle class="badge-ring" cx="314" cy="250" r="272" fill="var(--ring-white)"/>
      <g class="badge" clip-path="url(#badge-clip)">
        <rect x="40" y="-20" width="560" height="272" fill="var(--brand-orange)"/>
        <rect x="40" y="252" width="560" height="64" fill="var(--ring-white)"/>
        <rect x="40" y="316" width="560" height="62" fill="var(--brand-orange)"/>
        <rect x="40" y="378" width="560" height="140" fill="var(--board-dark)"/>
      </g>

      <text class="church-name" x="314" y="128">Thrive Church</text>
      <text class="headline" x="314" y="232">Grand Opening</text>
      <text class="event-time" x="314" y="297">10:30am | Sept. 26, 2021</text>
      <text class="event-address" x="314" y="357">4218 E. Marlowe Avenue</text>
      <text class="tagline" x="314" y="421">Multi-Ethnic Church</text>
      <text class="tagline" x="314" y="453">Planting Church</text>
    </g>
  </svg>
</main>
</body>
</html>
```